interior designer/stylist looking for a letter press business card to reflect the stylish work

Hello Designers,
I need a business card design for an company called Halvard Interior Design. I'm aiming at the high end residential and private client market in London providing sleek simple interiors. I'd like my business card to be tackboard worthy and expensive looking, i want people to pin it and for it to have a sought after look, and want prospective customers to hire me as their interior designer as my card is so beautiful.
I love letter press design. I also like the use of colour/foil on the edge.
Colour combos & general things I like -
Black and White
Navy Blue and Gold
Neutral colours (muted palette of greys whites navys beiges)
White Marble & brass
Morvane (fashion designer)
....also open to other suggestions....
Please dont take the pink in the attached photos too literally. i'd like the card to look more masculine than feminine.
I'd like Halvard on one side in one font, with interior design underneath so one word will make the statement....... unless anyone has any other ideas, open to suggestions.
I'd like a really simple font and for the whole card to look very graphic.
my details -
Petra Quillby
Interior Designer & Stylist
email petra@halvardinteriordesign.co.uk
phone +447813554019
website wwww.halvardinteriordesign.co.uk
GO GO GO!! EXCITED TO SEE THE OUTCOME!!
x L
Target Market(s)
High End Residential and private clients
Industry/Entity Type
Business
Contact Information for Business Card
Halvard Interior Design & Styling
Petra Quillby
phone +447813554019

```html
<!DOCTYPE html>
<html lang="en">
<head>
<meta charset="utf-8">
<title>Halvard Interior Design – Business Card</title>
<link rel="stylesheet" href="https://fonts.googleapis.com/css2?family=Fjalla+One&family=Lato:wght@400;700&display=swap">
<style>
  :root {
    --backdrop-top: #262626;
    --backdrop-bottom: #050505;
    --card-navy: #0f142e;
    --card-navy-back: #0d112d;
    --brand-yellow: #f6e71b;
    --text-white: #f2f2f2;
  }
  * { margin: 0; padding: 0; box-sizing: border-box; }
  html, body { width: 1200px; height: 900px; overflow: hidden; }
  body {
    position: relative;
    background: linear-gradient(to bottom, var(--backdrop-top) 0%, #1a1a1a 55%, var(--backdrop-bottom) 100%);
    font-family: "Lato", Arial, sans-serif;
  }
  .card {
    position: absolute;
    top: 184px;
    height: 491px;
    border-radius: 12px;
    text-align: center;
    box-shadow: 0 6px 18px rgba(0,0,0,0.45);
  }
  .card--front { left: 299px; width: 301px; background: var(--card-navy); }
  .card--back { left: 645px; width: 304px; background: var(--card-navy-back); }
  .brand-name {
    position: absolute;
    left: 0; right: 0;
    font-family: "Fjalla One", "Arial Narrow", sans-serif;
    font-weight: 400;
    color: var(--brand-yellow);
    line-height: 1.15;
  }
  .card--front .brand-name { top: 62px; font-size: 35px; }
  .card--back .brand-name { top: 190px; font-size: 37px; }
  .person { position: absolute; left: 0; right: 0; top: 237px; }
  .person__name {
    font-weight: 700;
    font-size: 19px;
    color: var(--brand-yellow);
    letter-spacing: 0.2px;
  }
  .person__role {
    margin-top: 4px;
    font-size: 13.5px;
    color: var(--text-white);
  }
  .contact {
    position: absolute;
    left: 0; right: 0;
    top: 362px;
    list-style: none;
    font-size: 13.5px;
    color: var(--text-white);
    line-height: 20px;
  }
  .contact__item { display: flex; justify-content: center; align-items: center; gap: 4px; }
  .contact__icon { width: 11px; height: 11px; fill: var(--brand-yellow); flex: none; }
</style>
</head>
<body>
  <section class="card card--front" aria-label="Business card front">
    <h1 class="brand-name">Halvard Interior<br>Design</h1>
    <div class="person">
      <p class="person__name">Petra Quillby</p>
      <p class="person__role">Interior Designer &amp; Stylist</p>
    </div>
    <ul class="contact">
      <li class="contact__item">
        <svg class="contact__icon" viewBox="0 0 12 12" aria-hidden="true"><path d="M1 4.5C1 3 3 2 6 2s5 1 5 2.5v1H8.5V4.3C7.7 4 4.3 4 3.5 4.3v1.2H1z"/><path d="M3 6h6l1.5 4h-9z"/></svg>
        <span>+447813554019</span>
      </li>
      <li class="contact__item">
        <svg class="contact__icon" viewBox="0 0 12 12" aria-hidden="true"><path d="M1 2.5h10v7H1z M1.6 3 6 6.6 10.4 3" fill="var(--brand-yellow)" stroke="var(--card-navy)" stroke-width="0.9"/></svg>
        <span>petra@halvardinteriordesign.co.uk</span>
      </li>
      <li class="contact__item">
        <svg class="contact__icon" viewBox="0 0 12 12" aria-hidden="true"><g fill="none" stroke="var(--brand-yellow)" stroke-width="1.6" stroke-linecap="round"><path d="M5 7 7 5"/><path d="M4.5 5.5 3 7a1.8 1.8 0 0 0 2.5 2.5L7 8"/><path d="M7.5 6.5 9 5a1.8 1.8 0 0 0-2.5-2.5L5 4"/></g></svg>
        <span>wwww.halvardinteriordesign.co.uk</span>
      </li>
    </ul>
  </section>

  <section class="card card--back" aria-label="Business card back">
    <h2 class="brand-name">Halvard Interior<br>Design</h2>
  </section>
</body>
</html>
```